brindle's business card for earthmoving and tipper hire business.

I have a small earthmoving and tipper truck company. I am aiming for the smaller jobs that the big guys don't want. I am also Doing grass slashing and fire hazard reduction work. I would like to see some earthy colors, greens browns etc. I have a tractor with a front end loader attachment, and a 22 ton tipper. I would like to maybe have a silhouette of a tipper and tractor/slasher/loader setup in centre with my business name over the top and details to one side or something like that

Industry/Entity Type

Business

Contact Information for Business Card

Brindle's yard digs and haulage hireToowoombaABN: 47781050480PH 0479126773Email brindle.4@fenwickmail.com

Font styles to use
Sans Serif

Colors
fbee3d
abd036
85cae6
f78f20

Requirements
Nice to have
• Earthy colors . business name in blue

```html
<!DOCTYPE html>
<html lang="en">
<head>
<meta charset="utf-8">
<title>Brindle's yard digs and haulage – business card</title>
<link rel="stylesheet" href="https://fonts.googleapis.com/css2?family=Questrial&display=swap">
<style>
  :root {
    --backdrop: #e4e2de;
    --card-dark: #3b4148;
    --card-dark-edge: #2c3136;
    --card-light: #ffffff;
    --ink: #30353b;
    --ink-soft: #d4d7da;
    --accent: #f78f20;
    --font: "Questrial", "Century Gothic", sans-serif;
  }
  * { box-sizing: border-box; margin: 0; padding: 0; }
  html, body {
    width: 1200px; height: 900px; overflow: hidden;
    background: var(--backdrop);
    font-family: var(--font);
  }
  .canvas { position: relative; width: 1200px; height: 900px; }

  .card {
    position: absolute;
    width: 660px; height: 378px;
    border-radius: 4px;
    box-shadow: 0 3px 0 rgba(0,0,0,.12), 0 14px 30px rgba(0,0,0,.18);
  }
  .card--back {
    left: 190px; top: 58px;
    background: linear-gradient(160deg, var(--card-dark) 0%, var(--card-dark-edge) 100%);
  }
  .card--front {
    left: 350px; top: 468px;
    background: var(--card-light);
  }

  /* service list */
  .services {
    position: absolute; left: 44px; top: 42px;
    list-style: none;
  }
  .services li {
    display: flex; align-items: center; gap: 10px;
    color: var(--ink-soft);
    font-size: 19px; letter-spacing: .4px;
    margin-bottom: 9px;
  }
  .tick { width: 18px; height: 18px; flex: none; }

  /* business name */
  .brand { position: absolute; line-height: 1.05; }
  .brand__name { display: block; font-size: 48px; letter-spacing: .5px; }
  .brand__line { display: block; font-size: 21px; letter-spacing: 1px; margin-top: 4px; color: var(--accent); }
  .card--back .brand { right: 44px; bottom: 70px; text-align: right; }
  .card--back .brand__name { color: var(--ink-soft); }
  .card--front .brand { left: 46px; top: 196px; }
  .card--front .brand__name { color: var(--ink); }

  /* contact details */
  .contact {
    position: absolute; left: 360px; top: 100px;
    list-style: none;
  }
  .contact li {
    display: flex; align-items: center; gap: 10px;
    color: var(--ink);
    font-size: 19px; letter-spacing: .5px;
    margin-bottom: 9px;
  }
  .contact .icon { width: 17px; height: 17px; flex: none; }
  .contact .abn-label { color: var(--accent); }
</style>
</head>
<body>
<main class="canvas">

  <section class="card card--back" aria-label="Card back">
    <ul class="services">
      <li><svg class="tick" viewBox="0 0 18 18"><rect x="1" y="3" width="13" height="13" fill="none" stroke="#f78f20" stroke-width="1.6"/><path d="M4 9l3.5 3.5L17 2" fill="none" stroke="#f78f20" stroke-width="2.4"/></svg>Small Earthworks</li>
      <li><svg class="tick" viewBox="0 0 18 18"><rect x="1" y="3" width="13" height="13" fill="none" stroke="#f78f20" stroke-width="1.6"/><path d="M4 9l3.5 3.5L17 2" fill="none" stroke="#f78f20" stroke-width="2.4"/></svg>Slashing</li>
      <li><svg class="tick" viewBox="0 0 18 18"><rect x="1" y="3" width="13" height="13" fill="none" stroke="#f78f20" stroke-width="1.6"/><path d="M4 9l3.5 3.5L17 2" fill="none" stroke="#f78f20" stroke-width="2.4"/></svg>Fire Hazards Reduction</li>
      <li><svg class="tick" viewBox="0 0 18 18"><rect x="1" y="3" width="13" height="13" fill="none" stroke="#f78f20" stroke-width="1.6"/><path d="M4 9l3.5 3.5L17 2" fill="none" stroke="#f78f20" stroke-width="2.4"/></svg>Rural Clean-ups</li>
      <li><svg class="tick" viewBox="0 0 18 18"><rect x="1" y="3" width="13" height="13" fill="none" stroke="#f78f20" stroke-width="1.6"/><path d="M4 9l3.5 3.5L17 2" fill="none" stroke="#f78f20" stroke-width="2.4"/></svg>Tipper</li>
    </ul>
    <p class="brand"><span class="brand__name">Brindle's</span><span class="brand__line">yard digs and haulage</span></p>
  </section>

  <section class="card card--front" aria-label="Card front">
    <p class="brand"><span class="brand__name">Brindle's</span><span class="brand__line">yard digs and haulage</span></p>
    <ul class="contact">
      <li><svg class="icon" viewBox="0 0 16 16"><path d="M8 1a5 5 0 0 0-5 5c0 3.6 5 9 5 9s5-5.4 5-9a5 5 0 0 0-5-5zm0 7a2 2 0 1 1 0-4 2 2 0 0 1 0 4z" fill="#f78f20"/></svg>Karrowan Vale</li>
      <li><svg class="icon" viewBox="0 0 16 16"><path d="M1 6c0-2 3-3.5 7-3.5S15 4 15 6v1.5h-3.5V5.8C10.5 5.5 9.3 5.4 8 5.4s-2.5.1-3.5.4v1.7H1z" fill="#f78f20"/><rect x="3" y="8.5" width="10" height="5.5" rx="1" fill="#f78f20"/><circle cx="8" cy="11.2" r="1.5" fill="#fff"/></svg>0438571629</li>
      <li><svg class="icon" viewBox="0 0 16 16"><rect x="1" y="3.5" width="14" height="9.5" rx="1" fill="#f78f20"/><path d="M1.5 4.2L8 9l6.5-4.8" fill="none" stroke="#fff" stroke-width="1.3"/></svg>brindle.4@fenwickmail.com</li>
      <li><span class="abn-label">ABN:</span> 62194038715</li>
    </ul>
  </section>

</main>
</body>
</html>
```